Maren's Atelier, Beauty & Therapy. New business in Verbier, Switzerland

Simple Flyer to put in evidence a particular service that the studio offers that is
EMS ( ELECTRIC MUSCLE STIMULATION)
There is a bike festival in Verbier ion the 12th of August and i would like to take an opportunity of this slot to advertise our new suit of EMS that can be very helpful for bike riders. The product is a suit with muscle electrostimulation, And there are many advantages and functionnality. For sportsmen and women, it can
I don't have any particular picture be cause the product is very new.
But i can send you some images for you to understand what it is, but if you find some images on the web it is better :)
I upload different versions of Logo, PLEASE FEEL FREE TO CHOOSE WHAT IS BEST :)
please check this link for more information about the product applied for bikers
https://www.pulsavo-fit.com/en/cycling-training-with-muscle-electrostimulation/
Updates
Hello Designers,
Here are a few details concerning the project;
- Maren's Atelier is not a reseller of the EMS suits, but we provide it as a service inside our studio.
- We wish to communicate on this new technology in order to bring a maximum of attention, not only for the suit, but also for the brand it self, since it is new in Verbier.
- for the flyer, i would like it to be simple, appealing, and without too much text.
- a french version of the same flyer is appreciated, without extra cost ;)
Thanks
Hello all designers,
thank you for all the good work.
For you who mentioned a date for the festival, i suggest please to take it off, and keep only " Alpenrad Pedal Days" if you want.
Thank you

```html
<!DOCTYPE html>
<html lang="en">
<head>
<meta charset="utf-8">
<title>Alpenrad Pedal Days – EMS Suit Flyer</title>
<link rel="stylesheet" href="https://fonts.googleapis.com/css2?family=Rubik+Dirt&family=Oswald:wght@200;500&family=Poppins:wght@400;500;600;800&display=swap">
<style>
  :root {
    --stage: #a3a3a3;
    --sky-light: #eaf7cf;
    --sky-mid: #d6efb0;
    --ridge-violet: #7a5fb0;
    --deep-violet: #3d1f78;
    --ink-violet: #2e0d5c;
    --night: #171717;
    --lilac: #9d88cc;
    --magenta: #8e2a82;
    --plum: #6e1a5e;
    --suit-circle: #7a2070;
    --white: #ffffff;
    --mint-arc: #e6f7d6;
  }
  * { margin: 0; padding: 0; box-sizing: border-box; }
  html, body { width: 848px; height: 1200px; overflow: hidden; background: var(--stage); }
  .flyer {
    position: absolute; left: 0; top: 51px;
    width: 848px; height: 1098px;
    background: var(--night);
    overflow: hidden;
    font-family: 'Poppins', sans-serif;
    color: var(--white);
  }
  .hero-photo {
    position: absolute; left: 0; top: 0; width: 848px; height: 580px;
    background: linear-gradient(180deg, var(--sky-light) 0%, var(--sky-mid) 28%, var(--ridge-violet) 34%, #5a3d9a 46%, var(--deep-violet) 62%, #2a1b3d 80%, var(--night) 100%);
  }
  .headline { position: absolute; left: 66px; top: 50px; }
  .headline text { font-family: 'Rubik Dirt', sans-serif; fill: var(--ink-violet); }
  .event-name {
    position: absolute; left: 76px; top: 250px;
    font-family: 'Rubik Dirt', sans-serif; font-size: 60px; line-height: 58px; font-weight: 400;
    color: var(--white);
  }
  .event-day {
    position: absolute; left: 68px; top: 385px;
    font-family: 'Rubik Dirt', sans-serif; font-size: 128px; line-height: 128px;
    color: var(--lilac); letter-spacing: -4px;
  }
  .event-month {
    position: absolute; left: 224px; top: 396px;
    font-family: 'Oswald', sans-serif; font-weight: 500; font-size: 50px; line-height: 52px;
    color: var(--magenta);
  }
  .event-year {
    position: absolute; left: 224px; top: 448px;
    font-family: 'Oswald', sans-serif; font-weight: 200; font-size: 50px; line-height: 56px;
    letter-spacing: 10px;
  }
  .offer-intro {
    position: absolute; left: 76px; top: 566px;
    font-weight: 800; font-size: 37px; line-height: 36px; letter-spacing: -0.5px;
  }
  .offer-intro .product { color: var(--magenta); display: block; }
  .offer-sub {
    position: absolute; left: 78px; top: 638px;
    font-weight: 500; font-size: 19px; letter-spacing: 5.2px;
  }
  .benefits { position: absolute; left: 84px; top: 685px; width: 320px; list-style: none; }
  .benefit {
    position: absolute; width: 140px;
    font-size: 16px; line-height: 19px; padding-left: 19px;
  }
  .benefit svg { position: absolute; left: 0; top: 3px; }
  .studio-name {
    position: absolute; left: 76px; top: 910px;
    display: flex; align-items: center; gap: 14px;
    font-weight: 600; font-size: 23px; letter-spacing: 4px;
  }
  .studio-name .dot { width: 50px; height: 50px; border: 2px solid var(--white); border-radius: 50%; }
  .visit-note {
    position: absolute; left: 78px; top: 980px;
    font-size: 11px; letter-spacing: 1.8px;
  }
  .visit-note b { font-weight: 600; }
  .url-band {
    position: absolute; left: 0; top: 1005px; width: 375px; height: 30px;
    background: var(--plum); border-radius: 0 15px 15px 0;
    padding-left: 77px; font-size: 18px; line-height: 30px; letter-spacing: 1.6px;
  }
  .url-band b { font-weight: 600; }
  .athletes { position: absolute; left: 400px; top: 600px; }
</style>
</head>
<body>
<main class="flyer">
  <div class="hero-photo" role="img" aria-label="Photo of a mountain biker riding at dusk against violet mountain ridges and a pale green sky"></div>

  <svg class="headline" width="710" height="160" viewBox="0 0 710 160" aria-label="Alpenrad">
    <text x="0" y="150" font-size="168" textLength="695" lengthAdjust="spacingAndGlyphs">ALPENRAD</text>
  </svg>

  <h2 class="event-name">PEDAL<br>DAYS</h2>
  <div class="event-day">12</div>
  <div class="event-month">AUGUST</div>
  <div class="event-year">2023</div>

  <h1 class="offer-intro">INTRODUCING THE NEW <span class="product">EMS SUIT</span></h1>
  <p class="offer-sub">ELECTRIC MUSCLE STIMULATION</p>

  <ul class="benefits">
    <li class="benefit" style="left:0;top:0"><svg width="14" height="14" viewBox="0 0 13 13"><rect x="1" y="1" width="11" height="11" rx="2" fill="none" stroke="#8e2a82" stroke-width="1.6"/><path d="M3.5 6.5l2.2 2.2 5-5.5" fill="none" stroke="#fff" stroke-width="1.6"/></svg>Used by sportsmen and women</li>
    <li class="benefit" style="left:162px;top:0"><svg width="14" height="14" viewBox="0 0 13 13"><rect x="1" y="1" width="11" height="11" rx="2" fill="none" stroke="#8e2a82" stroke-width="1.6"/><path d="M3.5 6.5l2.2 2.2 5-5.5" fill="none" stroke="#fff" stroke-width="1.6"/></svg>Strength training</li>
    <li class="benefit" style="left:0;top:76px"><svg width="14" height="14" viewBox="0 0 13 13"><rect x="1" y="1" width="11" height="11" rx="2" fill="none" stroke="#8e2a82" stroke-width="1.6"/><path d="M3.5 6.5l2.2 2.2 5-5.5" fill="none" stroke="#fff" stroke-width="1.6"/></svg>Pain management</li>
    <li class="benefit" style="left:162px;top:76px"><svg width="14" height="14" viewBox="0 0 13 13"><rect x="1" y="1" width="11" height="11" rx="2" fill="none" stroke="#8e2a82" stroke-width="1.6"/><path d="M3.5 6.5l2.2 2.2 5-5.5" fill="none" stroke="#fff" stroke-width="1.6"/></svg>Improved circulation</li>
    <li class="benefit" style="left:0;top:155px"><svg width="14" height="14" viewBox="0 0 13 13"><rect x="1" y="1" width="11" height="11" rx="2" fill="none" stroke="#8e2a82" stroke-width="1.6"/><path d="M3.5 6.5l2.2 2.2 5-5.5" fill="none" stroke="#fff" stroke-width="1.6"/></svg>Rehabilitation</li>
    <li class="benefit" style="left:162px;top:139px"><svg width="14" height="14" viewBox="0 0 13 13"><rect x="1" y="1" width="11" height="11" rx="2" fill="none" stroke="#8e2a82" stroke-width="1.6"/><path d="M3.5 6.5l2.2 2.2 5-5.5" fill="none" stroke="#fff" stroke-width="1.6"/></svg>Increased muscular endurance</li>
  </ul>

  <div class="studio-name"><span class="dot"></span>MAREN'S ATELIER</div>
  <p class="visit-note">VISIT OUR STUDIO TO <b>AVAIL THE SERVICE</b></p>
  <p class="url-band">www.<b>marensatelier</b>.com</p>

  <svg class="athletes" width="448" height="498" viewBox="0 0 448 498">
    <path d="M12 320 A240 240 0 0 1 420 120" fill="none" stroke="var(--mint-arc)" stroke-width="5"/>
    <circle cx="242" cy="318" r="232" fill="var(--suit-circle)" role="img" aria-label="Photo of a man and a woman wearing EMS training suits, arms raised"/>
  </svg>
</main>
</body>
</html>
```